Business Card Design

- one on one personal training
- group personal training
- indoor or outdoor training available
- fitness and health assessments
- personalised fitness programs
- flexible hours for training

I am a Personal Trainer in Perth Australia. I am looking to expand my word of mouth client base.

I would like to see something that uses the colours blue, green and/or yellow.

The final design should reflect the way that I train clients, fun, motivating and perhaps a little quirky?
Updates

update with a logo with the letters MPT thank you

Hi all, Have had some great designs so far. Have decided to go double sided, perhaps to use the back to list my services. Thank you

Please check update brief. Thank you.

Target Market(s)

Professionals, ages 30 to 60

Industry/Entity Type

Training

Contact Information for Business Card

Mira Ostrowski
Personal Trainer

0491 570 118
mirapersonaltrainer@quillnest.com
http://www.mirapersonaltrainer.net

Requirements
Must have
• A logo with the letter MPT
Nice to have
• a logo to represent either; fitness, health, change, overall well-being.
Should not have
• Please no weights or lotus flowers!!

```html
<!DOCTYPE html>
<html lang="en">
<head>
<meta charset="utf-8">
<title>Mira Ostrowski – Personal Trainer</title>
<link rel="stylesheet" href="https://fonts.googleapis.com/css2?family=Fira+Sans+Extra+Condensed:wght@700&family=Open+Sans:wght@400;600;700&display=swap">
<style>
  :root {
    --card: #ffffff;
    --ink: #111111;
    --logo-blue: #1f5fd8;
    --sun-yellow: #ffd400;
    --orange: #ff9a00;
    --lime: #7ed321;
    --sky: #3aaaf0;
    --dot-mint: #1fd39a;
    --dot-orange: #f7931e;
    --dot-yellow: #fcc30b;
    --dot-green: #8cc63f;
    --dot-blue: #29a9e1;
  }
  html, body {
    margin: 0;
    padding: 0;
    width: 1200px;
    height: 824px;
    overflow: hidden;
    background: var(--card);
  }
  .card {
    position: relative;
    width: 1200px;
    height: 824px;
    background: var(--card);
    color: var(--ink);
    font-family: "Open Sans", Arial, sans-serif;
    overflow: hidden;
  }
  .sun-burst {
    position: absolute;
    left: 620px;
    top: -250px;
    width: 560px;
    height: 560px;
    border-radius: 50%;
    background: radial-gradient(circle at 48% 62%, var(--sky) 0%, var(--sky) 26%, var(--orange) 48%, var(--sun-yellow) 72%, var(--lime) 100%);
  }
  .identity {
    position: absolute;
    left: 60px;
    width: 520px;
    top: 0;
    height: 824px;
    text-align: center;
  }
  .brand-mark {
    position: absolute;
    left: 150px;
    top: 200px;
    display: flex;
    align-items: center;
    gap: 14px;
  }
  .brand-mark__dot {
    width: 28px;
    height: 28px;
    border-radius: 50%;
    background: var(--lime);
  }
  .brand-mark__name {
    font-family: "Open Sans", Arial, sans-serif;
    font-weight: 700;
    font-size: 84px;
    line-height: 1;
    color: var(--logo-blue);
    letter-spacing: 1px;
  }
  .name {
    position: absolute;
    left: 0;
    width: 520px;
    top: 395px;
    margin: 0;
    font-family: "Fira Sans Extra Condensed", "Arial Narrow", sans-serif;
    font-weight: 700;
    font-size: 64px;
    line-height: 1;
  }
  .role {
    position: absolute;
    left: 0;
    width: 520px;
    top: 470px;
    margin: 0;
    font-size: 29px;
    line-height: 1;
  }
  .phone {
    position: absolute;
    left: 0;
    width: 520px;
    top: 568px;
    margin: 0;
    font-size: 27px;
    line-height: 1;
  }
  .web-contact {
    position: absolute;
    left: 0;
    width: 520px;
    top: 632px;
    margin: 0;
    font-size: 25px;
    line-height: 1.45;
    font-style: normal;
  }
  .services {
    position: absolute;
    left: 680px;
    top: 484px;
    margin: 0;
    padding: 0;
    list-style: none;
    font-size: 25px;
    line-height: 44px;
  }
  .services__item {
    display: flex;
    align-items: center;
    gap: 16px;
    white-space: nowrap;
  }
  .services__item::before {
    content: "";
    width: 18px;
    height: 18px;
    border-radius: 50%;
    background: var(--bullet);
    flex: none;
  }
  .services__item--mint { --bullet: var(--dot-mint); }
  .services__item--orange { --bullet: var(--dot-orange); }
  .services__item--yellow { --bullet: var(--dot-yellow); }
  .services__item--green { --bullet: var(--dot-green); }
  .services__item--blue { --bullet: var(--dot-blue); }
</style>
</head>
<body>
  <main class="card">
    <div class="sun-burst" role="img" aria-label="Decorative graphic of overlapping blue, orange, yellow and green circles"></div>

    <section class="identity">
      <div class="brand-mark">
        <span class="brand-mark__dot"></span>
        <span class="brand-mark__name">MPT</span>
      </div>
      <h1 class="name">Mira Ostrowski</h1>
      <p class="role">Personal Trainer</p>
      <p class="phone">Phone : 0491 570 118</p>
      <address class="web-contact">
        E-mail: mirapersonaltrainer@quillnest.com<br>
        Website: www.mirapersonaltrainer.net
      </address>
    </section>

    <ul class="services">
      <li class="services__item services__item--mint">One on one personal training</li>
      <li class="services__item services__item--orange">Group personal training</li>
      <li class="services__item services__item--yellow">Indoor or outdoor training available</li>
      <li class="services__item services__item--green">Fitness and health assessments</li>
      <li class="services__item services__item--blue">Personalised fitness programs</li>
    </ul>
  </main>
</body>
</html>
```